Web App Design Project

Need to provide graphical design of 2 web pages according to attached wireframes.

Colors should be adjusted for the 65+ population meaning not too bright.

App logo should be created as well - logo should represent long and good life.

Target Market(s)

65 years old and above

```html
<!DOCTYPE html>
<html lang="en">
<head>
<meta charset="utf-8">
<title>Home Measurements</title>
<link href="https://fonts.googleapis.com/css2?family=Arimo:wght@400;700&display=swap" rel="stylesheet">
<style>
:root{
  --page-bg:#d9dcd6;
  --green-top:#8cb882;
  --green-bottom:#4d8748;
  --green-text:#4e8f4a;
  --value-green:#4a8a46;
  --panel-grey:#f3f3f3;
  --divider:#e1e1e1;
  --card-border:#b9bccb;
  --text-dark:#5a5e70;
  --text-mid:#6b6f80;
  --nav-bg:#3c4055;
  --nav-active:#4c5064;
  --nav-line:#33374a;
  --nav-text:#c4c7d3;
  --chip:#8f93a3;
  --white:#ffffff;
}
*{box-sizing:border-box;margin:0;padding:0}
html,body{width:1200px;height:900px;overflow:hidden}
body{background:var(--page-bg);font-family:"Arimo",Arial,sans-serif;position:relative}
.app{position:absolute;left:100px;top:120px;width:1000px;height:660px;background:var(--white);box-shadow:0 10px 40px rgba(0,0,0,.25);overflow:hidden}
.topbar{position:absolute;left:0;top:0;width:1000px;height:60px;background:linear-gradient(var(--green-top),var(--green-bottom))}
.brand{position:absolute;left:0;top:0;width:200px;height:60px;border-right:1px solid rgba(255,255,255,.25)}
.brand-mark{position:absolute;left:22px;top:16px;width:26px;height:26px;border-radius:50%;background:var(--white)}
.brand-name{position:absolute;left:73px;top:13px;color:var(--white);font-weight:700;font-size:18px}
.brand-slogan{position:absolute;left:73px;top:34px;color:var(--white);font-size:9px}
.welcome{position:absolute;left:215px;top:20px;color:#eef4ea;font-size:16px}
.welcome b{color:var(--white)}
.font-sizes{position:absolute;left:610px;top:18px;color:#e6efe3;display:flex;align-items:baseline;gap:14px}
.font-sizes span:nth-child(1){font-size:11px}
.font-sizes span:nth-child(2){font-size:16px;font-weight:700;color:var(--white)}
.font-sizes span:nth-child(3){font-size:20px}
.search{position:absolute;left:686px;top:15px;width:162px;height:30px;background:rgba(255,255,255,.15);border:1px solid rgba(255,255,255,.35);border-radius:2px;color:#dfe9dc;font-size:14px;padding:8px 9px}
.search svg{position:absolute;right:8px;top:7px}
.top-btn{position:absolute;top:14px;height:31px;background:linear-gradient(#6a9e62,#467a41);border:1px solid rgba(0,0,0,.15);border-radius:2px;color:var(--white);font-weight:700;font-size:16px;text-align:center;line-height:29px}
.help{left:888px;width:32px}
.exit{left:934px;width:52px}
.subbar{position:absolute;left:0;top:60px;width:1000px;height:70px;background:var(--panel-grey)}
.section-title{position:absolute;left:16px;top:26px;color:var(--green-text);font-weight:700;font-size:17px}
.subbar-divider{position:absolute;left:199px;top:0;width:1px;height:70px;background:var(--divider)}
.add-measure{position:absolute;left:230px;top:23px;display:flex;align-items:center;gap:7px;color:var(--green-text);font-weight:700;font-size:15px}
.settings{position:absolute;left:944px;top:22px}
.sidebar{position:absolute;left:0;top:130px;width:200px;height:400px;background:var(--panel-grey);border-right:1px solid var(--divider)}
.tab{position:absolute;left:10px;width:190px;height:90px;display:flex;align-items:center;gap:14px;color:var(--text-dark);font-weight:700;font-size:16px;padding-left:30px}
.tab.active{background:var(--white);box-shadow:0 2px 4px rgba(0,0,0,.12)}
.tab.sugar{top:0}
.tab.pressure{top:100px}
.entry{position:absolute;left:229px;width:742px;height:62px;border:1px solid var(--card-border);border-radius:3px;background:var(--white)}
.entry-date{position:absolute;left:14px;top:22px;color:var(--text-dark);font-weight:700;font-size:15px}
.entry-note{position:absolute;left:148px;top:22px;color:var(--text-mid);font-size:16px}
.entry-chip{position:absolute;left:148px;top:16px;height:29px;padding:0 8px;background:var(--chip);border-radius:2px;color:var(--white);font-weight:700;font-size:13px;line-height:29px}
.entry-value{position:absolute;left:576px;top:22px;color:var(--value-green);font-weight:700;font-size:16px}
.entry-info{position:absolute;left:700px;top:21px}
.bottom-nav{position:absolute;left:0;top:530px;width:1000px;height:130px;background:var(--nav-bg);display:flex}
.nav-item{flex:1;position:relative;border-right:1px solid var(--nav-line);color:var(--nav-text);font-weight:700;font-size:14px;text-align:center;line-height:17px}
.nav-item:last-child{border-right:none}
.nav-item.active{background:var(--nav-active);color:var(--white)}
.nav-item svg{position:absolute;left:50%;top:30px;transform:translateX(-50%)}
.nav-label{position:absolute;left:0;right:0;top:82px}
.nav-label.two{top:74px}
</style>
</head>
<body>
<main class="app">
  <header class="topbar">
    <div class="brand">
      <span class="brand-mark"></span>
      <span class="brand-name">AppName</span>
      <span class="brand-slogan">Here is your slogan</span>
    </div>
    <div class="welcome">Welcome back, <b>Walter Grant</b></div>
    <div class="font-sizes"><span>A</span><span>A</span><span>A</span></div>
    <div class="search">Search
      <svg width="16" height="16" viewBox="0 0 16 16"><circle cx="6.5" cy="6.5" r="4.8" fill="none" stroke="#dfe9dc" stroke-width="2"/><line x1="10" y1="10" x2="14.5" y2="14.5" stroke="#dfe9dc" stroke-width="2.4"/></svg>
    </div>
    <div class="top-btn help">?</div>
    <div class="top-btn exit">Exit</div>
  </header>

  <section class="subbar">
    <div class="section-title">Home Measurements</div>
    <div class="subbar-divider"></div>
    <div class="add-measure">
      <svg width="26" height="26" viewBox="0 0 26 26"><circle cx="13" cy="13" r="11.5" fill="none" stroke="#4e8f4a" stroke-width="2"/><path d="M13 7v12M7 13h12" stroke="#4e8f4a" stroke-width="3"/></svg>
      Add measurement
    </div>
    <svg class="settings" width="26" height="26" viewBox="0 0 26 26"><circle cx="13" cy="13" r="11.5" fill="none" stroke="#5a5e70" stroke-width="2"/><circle cx="13" cy="13" r="5" fill="none" stroke="#5a5e70" stroke-width="3.5" stroke-dasharray="2.4 1.5"/><circle cx="13" cy="13" r="2" fill="#5a5e70"/></svg>
  </section>

  <nav class="sidebar">
    <div class="tab active sugar">
      <svg width="22" height="32" viewBox="0 0 22 32"><path d="M11 1C8 10 1 16 1 22a10 10 0 0 0 20 0C21 16 14 10 11 1z" fill="#5a5e70"/><path d="M7 21a5 5 0 0 0 4 6" fill="none" stroke="#fff" stroke-width="1.6"/></svg>
      Sugar Level
    </div>
    <div class="tab pressure">
      <svg width="32" height="32" viewBox="0 0 32 32"><circle cx="16" cy="16" r="14" fill="none" stroke="#5a5e70" stroke-width="3"/><path d="M16 16l6-7" stroke="#5a5e70" stroke-width="2.6"/><circle cx="16" cy="16" r="2.2" fill="#5a5e70"/></svg>
      Pressure
    </div>
  </nav>

  <div class="entry" style="top:160px">
    <span class="entry-date">01/01/2013</span>
    <span class="entry-note">My Sugar Level</span>
    <span class="entry-value">6,3 mmol/l</span>
    <svg class="entry-info" width="20" height="20" viewBox="0 0 20 20"><circle cx="10" cy="10" r="9" fill="none" stroke="#a6a9b6"/><text x="10" y="15" text-anchor="middle" font-family="Georgia,serif" font-style="italic" font-size="12" fill="#a6a9b6">i</text></svg>
  </div>
  <div class="entry" style="top:252px">
    <span class="entry-date">02/21/2013</span>
    <span class="entry-chip">Add comment</span>
    <span class="entry-value">7,9 mmol/l</span>
    <svg class="entry-info" width="20" height="20" viewBox="0 0 20 20"><circle cx="10" cy="10" r="9" fill="none" stroke="#a6a9b6"/><text x="10" y="15" text-anchor="middle" font-family="Georgia,serif" font-style="italic" font-size="12" fill="#a6a9b6">i</text></svg>
  </div>

  <footer class="bottom-nav">
    <div class="nav-item">
      <svg width="32" height="34" viewBox="0 0 32 34"><rect x="4" y="2" width="10" height="22" rx="5" transform="rotate(-20 9 13)" fill="none" stroke="#c4c7d3" stroke-width="2"/><rect x="14" y="10" width="10" height="22" rx="5" transform="rotate(40 19 21)" fill="#c4c7d3"/></svg>
      <span class="nav-label">Medications</span>
    </div>
    <div class="nav-item active">
      <svg width="32" height="34" viewBox="0 0 32 34"><path d="M24 2l6 6L11 27l-6 1 1-6z" fill="none" stroke="#fff" stroke-width="2"/><path d="M5 28l-3 4" stroke="#fff" stroke-width="2"/><path d="M15 11l2 2M18 8l2 2M12 14l2 2" stroke="#fff" stroke-width="1.5"/></svg>
      <span class="nav-label two">Home<br>Measurements</span>
    </div>
    <div class="nav-item">
      <svg width="32" height="34" viewBox="0 0 32 34"><rect x="1" y="5" width="30" height="27" fill="none" stroke="#c4c7d3" stroke-width="2"/><rect x="1" y="5" width="30" height="6" fill="#c4c7d3"/><path d="M8 1v7M24 1v7M16 1v7" stroke="#c4c7d3" stroke-width="2.4"/><text x="16" y="27" text-anchor="middle" font-family="Arimo,sans-serif" font-size="12" fill="#c4c7d3">17</text></svg>
      <span class="nav-label">My Schedule</span>
    </div>
    <div class="nav-item">
      <svg width="34" height="34" viewBox="0 0 34 34"><rect x="2" y="2" width="30" height="22" fill="none" stroke="#c4c7d3" stroke-width="2"/><path d="M6 15h6l3-6 4 10 3-6h6" fill="none" stroke="#c4c7d3" stroke-width="1.6"/><path d="M17 24v2M11 33l6-7 6 7" fill="none" stroke="#c4c7d3" stroke-width="2"/></svg>
      <span class="nav-label">Lab Test Results</span>
    </div>
    <div class="nav-item">
      <svg width="34" height="34" viewBox="0 0 34 34"><g fill="none" stroke="#c4c7d3" stroke-width="2"><rect x="2" y="2" width="6" height="6"/><rect x="2" y="14" width="6" height="6"/><rect x="2" y="26" width="6" height="6"/></g><g fill="#c4c7d3"><rect x="13" y="3" width="20" height="4"/><rect x="13" y="15" width="20" height="4"/><rect x="13" y="27" width="20" height="4"/></g></svg>
      <span class="nav-label two">Checkups &amp;<br>Procedures</span>
    </div>
    <div class="nav-item">
      <svg width="34" height="34" viewBox="0 0 34 34"><circle cx="17" cy="10" r="8" fill="#c4c7d3"/><path d="M1 34c0-9 7-14 16-14s16 5 16 14z" fill="#c4c7d3"/></svg>
      <span class="nav-label">My Profile</span>
    </div>
    <div class="nav-item">
      <svg width="34" height="30" viewBox="0 0 34 30"><path d="M17 29S1 19 1 9a8 8 0 0 1 16-2 8 8 0 0 1 16 2c0 10-16 20-16 20z" fill="#c4c7d3"/></svg>
      <span class="nav-label two">My Health Care<br>Providers</span>
    </div>
  </footer>
</main>
</body>
</html>
```